Standout Business Card for Recruiting New Hires

JOIN A WINNING TEAM! We are a nationally recognized Top Contractor for Paving and Parking Lot Maintenance. Our people are our most valuable asset, helping us to achieve Our Vision of building the best commercial pavement services company to benefit the best owners, the best employees and the best customers.

We want to create a Business Card to help us capture potential new hires, whenever and wherever they are discovered. This is not a traditional business card with someone's name it, only our Company Name and the information provided below.

Target Market(s)

Exceptional, standout, customer service oriented employees currently working elsewhere...at our competitors, at the car wash, in the deli, at the restaurant, in an airport, driving an Tripzel...wherever we find them.

Industry/Entity Type

Construction Company

Contact Information for Business Card

A double sided business card, with the standout feature being "Join A Winning Team" and the benefits listed somewhere on the card.

Requirements
Must have
• -Call to Action (Join a Winning Team)
• -Our Logo
• -Our Physical Address (17B Harrow Court, Clinton, CT 06287)
• -Our Website (www.BrightfieldSurfacing.com)
• -Our Phone Number (860) 555-0147.
• -Our Bullet Points (can be altered):
• - Competitive Pay
• - Full Time, Consistent Work Schedule
• - Paid Overtime / Drive Time
• - Work with Great People in a Great Environment
• - Training Program
• Something like that.
Nice to have
• Maybe it could say, "Come and Join Connecticut's Top Rated Paving Contractor" or Come grow with us. Something like that.
Should not have
• Anyone's name on it. This is a generic card for anyone at the company to give to a potential employee! (I have attached a business card sample, just to illustrate our look and feel).

```html
<!DOCTYPE html>
<html lang="en">
<head>
<meta charset="utf-8">
<title>Brightfield Surfacing Services – Recruiting Card</title>
<link rel="stylesheet" href="https://fonts.googleapis.com/css2?family=Open+Sans:wght@400;600;700;800&display=swap">
<style>
  :root {
    --ink: #1a1a1a;
    --red: #d0222f;
    --paper: #ffffff;
    --backdrop: #2b2b2d;
    --rule: #222222;
  }
  * { margin: 0; padding: 0; box-sizing: border-box; }
  html, body { width: 1200px; height: 900px; overflow: hidden; }
  body {
    background: var(--backdrop);
    font-family: "Open Sans", Arial, sans-serif;
    color: var(--ink);
    position: relative;
  }
  .card {
    position: absolute;
    width: 560px;
    height: 320px;
    background: var(--paper);
    border-radius: 20px;
    overflow: hidden;
    box-shadow: 0 10px 30px rgba(0,0,0,.45);
  }
  .card--front { left: 60px; top: 110px; }
  .card--back  { left: 580px; top: 470px; }
  .card__shapes { position: absolute; inset: 0; }

  .brand { position: absolute; left: 34px; top: 40px; display: flex; align-items: center; gap: 12px; }
  .brand__dot { width: 34px; height: 34px; border-radius: 50%; background: var(--red); flex: none; }
  .brand__name {
    font-weight: 800; font-size: 30px; line-height: 1; color: var(--ink);
    letter-spacing: -.5px;
  }
  .brand__name small { display: block; font-size: 17px; letter-spacing: 1.6px; margin-top: 4px; font-weight: 800; }

  .tagline {
    position: absolute; left: 34px; top: 122px;
    color: var(--red); font-weight: 600; font-size: 12.5px; letter-spacing: .2px;
    text-transform: uppercase;
  }

  .benefits { position: absolute; right: 30px; top: 150px; text-align: right; list-style: none; }
  .benefits__title { color: var(--red); font-weight: 600; font-size: 14px; margin-bottom: 2px; display: block; }
  .benefits li.benefits__item {
    font-size: 12px; line-height: 17px; display: flex; justify-content: flex-end; align-items: center; gap: 8px;
  }
  .benefits li.benefits__item::after {
    content: ""; width: 7px; height: 7px; border-radius: 50%; background: var(--red); flex: none;
  }

  .cta {
    position: absolute; right: 14px; top: 203px;
    color: var(--paper); font-size: 12px; font-weight: 600; letter-spacing: .8px; text-transform: uppercase;
  }

  .contacts { position: absolute; left: 30px; top: 218px; list-style: none; }
  .contacts li { display: flex; align-items: center; gap: 8px; font-size: 12px; line-height: 15px; }
  .contacts svg { width: 9px; height: 9px; fill: var(--red); flex: none; }
</style>
</head>
<body>

<section class="card card--front" aria-label="Card front">
  <svg class="card__shapes" viewBox="0 0 560 320" aria-hidden="true">
    <polygon points="0,282 230,282 256,302 560,302 560,320 0,320" fill="var(--ink)"/>
    <polygon points="256,295 560,280 560,302 256,302" fill="var(--red)"/>
  </svg>
  <div class="brand">
    <span class="brand__dot"></span>
    <p class="brand__name">Brightfield<small>SURFACING SERVICES</small></p>
  </div>
  <p class="tagline">Come and join Connecticut's top rated paving contractor</p>
  <ul class="benefits">
    <li class="benefits__title">SERVICES</li>
    <li class="benefits__item">Competitive Pay</li>
    <li class="benefits__item">Full Time, Consistent Work Schedule</li>
    <li class="benefits__item">Paid Overtime / Drive Time</li>
    <li class="benefits__item">Work with Great People in a Great Environment</li>
    <li class="benefits__item">Training Program</li>
    <li class="benefits__item">Something like that</li>
  </ul>
</section>

<section class="card card--back" aria-label="Card back">
  <svg class="card__shapes" viewBox="0 0 560 320" aria-hidden="true">
    <line x1="30" y1="210" x2="375" y2="210" stroke="var(--rule)" stroke-width="1.5"/>
    <polygon points="375,190 560,190 560,232 375,232" fill="var(--ink)"/>
    <polygon points="375,232 560,232 560,240 368,240" fill="var(--red)"/>
    <polygon points="0,308 290,308 375,240 375,250 296,316 0,316" fill="var(--red)"/>
  </svg>
  <div class="brand">
    <span class="brand__dot"></span>
    <p class="brand__name">Brightfield<small>SURFACING SERVICES</small></p>
  </div>
  <p class="cta">Join a Winning Team</p>
  <ul class="contacts">
    <li><svg viewBox="0 0 10 10"><path d="M2 0h2l1 3-1.5 1a6 6 0 0 0 2.5 2.5L7 5l3 1v2c0 1-1 2-2 2A8 8 0 0 1 0 2c0-1 1-2 2-2z"/></svg>(860) 555-0147</li>
    <li><svg viewBox="0 0 10 10"><rect x="1" y="3" width="8" height="6" rx="1"/><rect x="3" y="0" width="4" height="3"/></svg>860.555.0192</li>
    <li><svg viewBox="0 0 10 10"><rect x="2.5" y="0" width="5" height="10" rx="1"/></svg>203.555.0163</li>
    <li><svg viewBox="0 0 10 10"><path d="M0 2h10v6H0z M0 2l5 3 5-3" fill="none" stroke="var(--red)" stroke-width="1.2"/></svg>careers@brightfieldsurfacing.com</li>
    <li><svg viewBox="0 0 10 10"><circle cx="5" cy="5" r="5"/></svg>www.BrightfieldSurfacing.com</li>
    <li><svg viewBox="0 0 10 10"><path d="M5 0a3.5 3.5 0 0 1 3.5 3.5C8.5 6 5 10 5 10S1.5 6 1.5 3.5A3.5 3.5 0 0 1 5 0z"/></svg>17B Harrow Court Clinton, CT 06287</li>
  </ul>
</section>

</body>
</html>
```